Quarrow financial services, is a financial company that provides consultancy, brokerage services, and funding.

we will be providing the clients with insights, knowledge and data with regards to the financial markets.

with the brokerage services we will try to find the suitable counterparts that provide them with the best investments that suits their needs and expected return.

Target Market(s)

financial institutions, Corporates, high-net worth individuals

Industry/Entity Type

Financial Service

Contact Information for Business Card

Font styles to use
Other font styles liked:
• applemyungjo

Colors
00a990
848484

Requirements
Must have
• the logo at the back
Nice to have
• Finesse
Should not have
• boldness

```html
<!DOCTYPE html>
<html lang="en">
<head>
<meta charset="utf-8">
<title>Quarrow Financial Services – Business Card</title>
<link rel="stylesheet" href="https://fonts.googleapis.com/css2?family=Cinzel:wght@400&family=Open+Sans:wght@400;600&display=swap">
<style>
  :root {
    --stage: #e9e7e4;
    --card: #0e0e0e;
    --card-edge: #1c1c1c;
    --ink-light: #e4e4e4;
    --ink-grey: #bdbdbd;
    --accent-green: #7fb046;
    --mark-pale: #d9e6cf;
    --divider: #3a3a3a;
  }
  * { box-sizing: border-box; margin: 0; padding: 0; }
  html, body { width: 1200px; height: 844px; overflow: hidden; }
  body {
    background: var(--stage);
    font-family: "Open Sans", Arial, sans-serif;
    position: relative;
  }
  .card {
    position: absolute;
    top: 268px;
    width: 540px;
    height: 309px;
    background: var(--card);
    border: 1px solid var(--card-edge);
    border-radius: 3px;
    box-shadow: 0 6px 18px rgba(0,0,0,.25);
  }
  .card--front { left: 45px; }
  .card--back { left: 615px; }

  .brand {
    position: absolute;
    display: flex;
    align-items: center;
    gap: 14px;
  }
  .brand__square {
    width: 34px;
    height: 34px;
    background: var(--mark-pale);
  }
  .brand__name {
    font-family: "Cinzel", "Times New Roman", serif;
    font-weight: 400;
    color: var(--ink-grey);
    font-size: 21px;
    letter-spacing: 2px;
    line-height: 1;
    white-space: nowrap;
  }
  .card--front .brand { left: 96px; top: 70px; }
  .card--back .brand { left: 50%; top: 50%; transform: translate(-50%, -50%); }

  .holder {
    position: absolute;
    right: 296px;
    top: 178px;
    text-align: right;
    color: var(--ink-light);
  }
  .holder__name {
    color: var(--accent-green);
    font-weight: 600;
    font-size: 17px;
    line-height: 1.2;
  }
  .holder__role { font-size: 13px; margin-bottom: 12px; }
  .holder__address { font-size: 13px; line-height: 1.35; font-style: normal; }

  .divider {
    position: absolute;
    left: 260px;
    top: 150px;
    width: 1px;
    height: 110px;
    background: var(--divider);
  }

  .contacts {
    position: absolute;
    left: 278px;
    top: 152px;
    list-style: none;
    color: var(--ink-light);
    font-size: 13px;
  }
  .contacts__item {
    display: flex;
    align-items: center;
    gap: 9px;
    height: 22px;
  }
  .contacts__icon { width: 11px; height: 11px; fill: var(--accent-green); flex: none; }
</style>
</head>
<body>

  <section class="card card--front" aria-label="Business card front">
    <div class="brand">
      <span class="brand__square"></span>
      <span class="brand__name">Quarrow Financial Services</span>
    </div>

    <div class="holder">
      <p class="holder__name">Daniel Harwick</p>
      <p class="holder__role">Managing Director</p>
      <address class="holder__address">P.O. Box 3817, Linden<br>Falls, OR 97482</address>
    </div>

    <span class="divider"></span>

    <ul class="contacts">
      <li class="contacts__item">
        <svg class="contacts__icon" viewBox="0 0 12 12"><path d="M2.5 1l2 2.2-1 1.3c.7 1.5 1.8 2.6 3.2 3.3l1.3-1 2.2 2-1.2 1.6C5 10 2 7 1 2.3z"/></svg>
        (055)-318-2047
      </li>
      <li class="contacts__item">
        <svg class="contacts__icon" viewBox="0 0 12 12"><path d="M3.5 0.5h5v11h-5z M4.5 1.5v8h3v-8z"/></svg>
        214-630-5821
      </li>
      <li class="contacts__item">
        <svg class="contacts__icon" viewBox="0 0 12 12"><path d="M0.5 2.5h11v7h-11z"/><path d="M0.8 2.8L6 6.5l5.2-3.7" stroke="#0e0e0e" stroke-width="1" fill="none"/></svg>
        hello@quarrowfs.com
      </li>
      <li class="contacts__item">
        <svg class="contacts__icon" viewBox="0 0 12 12"><circle cx="6" cy="6" r="5.5"/></svg>
        www.quarrowfs.com
      </li>
    </ul>
  </section>

  <section class="card card--back" aria-label="Business card back">
    <div class="brand">
      <span class="brand__square"></span>
      <span class="brand__name">Quarrow Financial Services</span>
    </div>
  </section>

</body>
</html>
```